Brochure for The Lodge Nest a Vacation Rental company in Miami

The Lodge Nest is a vacation rental company in Miami. We specialize in vacation rentals and hotel-alternative rentals for travelers of all types.
We are looking for a modern and sleek brochure to help us promote our business and property management. This brochure will help persuade property owners to allow us to manage and operate their property as a vacation home.
We are looking for large images of luxury properties, modern sleek lines, modern text like "raleway" or "proxima nova" or something similar.
Target Market(s)
Property owners. We are a vacation rental management company.
Industry/Entity Type
Hotel
Font styles to use
Other font styles liked:
- Proxima nova or Raleway or brandon grotesque, or something similar
Requirements
Must have
- modern sleek design. Nice spacing and wonderful photos.
- Here's an example Brochure we liked in terms of design. Nothing to do with our industry, just the design style: http://www.quorvelhome.com/download/quorvel_brochure.pdf
- I HAVE INCLUDED THE FOLLOWING FILES:
- - logo files
- - screen shots of website designs that I like for design inspiration
- - content you can use for the brochure about our company and other information etc
- - images of properties we manage

```html
<!DOCTYPE html>
<html lang="en">
<head>
<meta charset="utf-8">
<title>The Lodge Nest – Owner Brochure</title>
<link rel="stylesheet" href="https://fonts.googleapis.com/css2?family=Raleway:wght@400;500;600;700;800&display=swap">
<style>
  :root {
    --bg: #e9ebee;
    --paper: #ffffff;
    --brand-blue: #3f86c4;
    --brand-blue-dark: #2d6ea8;
    --ink: #3a3f45;
    --ink-soft: #6b7178;
    --photo-sky: #9cc6e6;
    --photo-pool: #5fb3d6;
    --photo-green: #5f8a4a;
    --photo-night: #1f2a44;
    --photo-glow: #c7a25a;
  }
  * { box-sizing: border-box; margin: 0; padding: 0; }
  html, body { width: 900px; height: 1200px; overflow: hidden; }
  body {
    background: var(--bg);
    font-family: "Raleway", Arial, sans-serif;
    color: var(--ink);
    position: relative;
  }
  .spread {
    position: absolute;
    left: 40px;
    width: 820px;
    height: 530px;
    display: flex;
    background: var(--paper);
    box-shadow: 0 6px 18px rgba(0,0,0,.18);
  }
  .spread--cover { top: 40px; }
  .spread--inside { top: 630px; }
  .page { position: relative; width: 410px; height: 100%; overflow: hidden; }

  .logo {
    display: flex; align-items: center; gap: 8px;
    font-weight: 600; font-size: 15px; letter-spacing: .5px;
  }
  .logo__dot { width: 10px; height: 10px; border-radius: 50%; background: currentColor; }

  /* Cover – back page */
  .cover-back__head {
    height: 70px; padding: 26px 24px; color: var(--brand-blue-dark);
    background: var(--paper);
  }
  .cover-back__photo {
    position: absolute; left: 0; top: 70px; width: 100%; height: 460px;
    background: linear-gradient(180deg, var(--photo-sky) 0%, var(--photo-green) 38%, var(--photo-pool) 62%, #3e90bf 100%);
  }
  .cover-back__tint {
    position: absolute; inset: 0;
    background: linear-gradient(90deg, rgba(63,134,196,.25), rgba(63,134,196,0));
  }

  /* Cover – front page */
  .cover-front__head {
    height: 70px; padding: 26px 24px; background: var(--brand-blue); color: #fff;
  }
  .cover-front__photo {
    height: 300px;
    background: linear-gradient(180deg, #d8ecf8 0%, var(--photo-sky) 45%, #f2f4f6 70%, #c9d3db 100%);
  }
  .cover-front__band {
    height: 160px; background: var(--brand-blue); color: #fff;
    padding: 38px 28px;
  }
  .cover-front__title {
    font-size: 17px; font-weight: 700; letter-spacing: 1px; text-transform: uppercase;
    border-top: 1px solid rgba(255,255,255,.7); border-bottom: 1px solid rgba(255,255,255,.7);
    padding: 8px 0; text-align: center;
  }
  .cover-front__text { margin-top: 12px; font-size: 10.5px; line-height: 1.5; text-align: center; }

  /* Inside – left */
  .inside-left__bar { height: 16px; background: var(--brand-blue); }
  .inside-left__city {
    height: 260px;
    background: linear-gradient(180deg, var(--photo-night) 0%, #2f4466 60%, var(--photo-glow) 100%);
  }
  .inside-left__pool {
    height: 254px;
    background: linear-gradient(180deg, var(--photo-green) 0%, #8fb8cf 40%, var(--photo-pool) 70%, #cfe4ef 100%);
  }

  /* Inside – right */
  .inside-right { padding: 30px 28px 20px 26px; }
  .section-head { display: flex; align-items: center; gap: 10px; }
  .section-head__rule { flex: 1; height: 2px; background: var(--brand-blue); }
  .section-head__label { font-size: 13px; font-weight: 800; color: var(--ink); letter-spacing: .5px; }
  .section-title { font-size: 16px; font-weight: 800; color: var(--ink); letter-spacing: .5px; margin-top: 2px; }
  .body-copy { font-size: 8.6px; line-height: 1.5; color: var(--ink-soft); margin-top: 9px; }
  .section-head--why { margin-top: 20px; }
  .benefits { list-style: none; margin-top: 8px; }
  .benefits li { font-size: 8.6px; line-height: 1.5; color: var(--ink-soft); margin-bottom: 6px; padding-left: 12px; position: relative; }
  .benefits li::before {
    content: ""; position: absolute; left: 0; top: 4px; width: 5px; height: 5px; background: var(--brand-blue);
  }
  .benefits strong { color: var(--ink); font-weight: 700; }
</style>
</head>
<body>

<section class="spread spread--cover">
  <div class="page cover-back">
    <div class="cover-back__head">
      <div class="logo"><span class="logo__dot"></span>The Lodge Nest</div>
    </div>
    <div class="cover-back__photo" role="img" aria-label="Luxury rooftop pool with palm trees and lounge chairs">
      <div class="cover-back__tint"></div>
    </div>
  </div>
  <div class="page cover-front">
    <div class="cover-front__head">
      <div class="logo"><span class="logo__dot"></span>The Lodge Nest</div>
    </div>
    <div class="cover-front__photo" role="img" aria-label="Glass balcony overlooking the Miami waterfront"></div>
    <div class="cover-front__band">
      <h1 class="cover-front__title">Creating a Personalized Travel Experience</h1>
      <p class="cover-front__text">We specialize in vacation rentals and hotel-alternative rentals for travelers of all types.</p>
    </div>
  </div>
</section>

<section class="spread spread--inside">
  <div class="page inside-left">
    <div class="inside-left__bar"></div>
    <div class="inside-left__city" role="img" aria-label="Miami high-rise skyline at dusk with lit pool deck"></div>
    <div class="inside-left__pool" role="img" aria-label="Resort pool with loungers and palm trees"></div>
  </div>
  <div class="page inside-right">
    <div class="section-head">
      <span class="section-head__label">OWNERS:</span>
      <span class="section-head__rule"></span>
    </div>
    <h2 class="section-title">BECOME A PARTNER</h2>
    <p class="body-copy">As an owner of a luxury property in a vacation destination you understand the value of your prized asset. Partnering with The Lodge Nest is the most effective way to maximize the revenue your property generates.</p>
    <p class="body-copy">As your local vacation rental partner we handle guest care, cleaning, pricing and upkeep so your home earns more while staying in perfect condition.</p>
    <p class="body-copy">Are you interested in working with The Lodge Nest?</p>

    <div class="section-head section-head--why">
      <span class="section-title">WHY BECOME OUR PARTNER:</span>
      <span class="section-head__rule"></span>
    </div>
    <ul class="benefits">
      <li><strong>Selective Process:</strong> We hand-pick only the best properties, accepting less than 20% of the homes we review. This keeps our collection refined and guest demand high.</li>
      <li><strong>Pay-for-Performance Model:</strong> Our fee is a share of booked revenue, so we only earn when you earn.</li>
      <li><strong>Full Transparency:</strong> Owners see every booking, payout and review through a simple online portal.</li>
      <li><strong>Local Team:</strong> Our Miami staff is on call around the clock for guests and owners.</li>
      <li><strong>We Take Care of the Details:</strong> From linens to licensing, we manage everything needed to showcase and protect your home.</li>
    </ul>
  </div>
</section>

</body>
</html>
```